Velvor IT Services Business Card

Velvor IT Services are a Perth based IT Services company. We would like to incorporate our company logo (attached) and stick with the blue that is in that design. I would like a clean look design that isn't too busy, yet creates a lasting image that is instantly recognisable in the recipients mind.

Target Market(s)

The target audience is small/medium business owners.

Industry/Entity Type

Business

Font styles to use
Serif
Sans Serif

Colors

Designer to choose colors to be used in the design.

Requirements
Must have
• The design should include:
Business name: Velvor IT Services
Directors Name: Marcus Dredge
Phone Number: 0483 906 452
Email: support@velvorit.com.au
Website: www.velvorit.com.au

```html
<!DOCTYPE html>
<html lang="en">
<head>
<meta charset="utf-8">
<title>Velvor IT Services – Business Card</title>
<link href="https://fonts.googleapis.com/css2?family=Arimo:wght@400;700&display=swap" rel="stylesheet">
<style>
  :root {
    --stage: #d9d9d9;
    --frame: #3b3b3b;
    --frame-line: #ffffff;
    --face-light: #f4f4f4;
    --face-mid: #dcdcdc;
    --row: #e4e4e4;
    --brand-blue: #3a9ad9;
    --brand-deep: #1f5fae;
    --ink: #2a2a2a;
    --white: #ffffff;
  }
  * { box-sizing: border-box; margin: 0; padding: 0; }
  html, body {
    width: 1200px; height: 768px; overflow: hidden;
    background: var(--stage);
    font-family: "Arimo", Arial, sans-serif;
  }
  .canvas {
    width: 1200px; height: 768px;
    display: flex; align-items: center; justify-content: center; gap: 40px;
  }
  .card {
    width: 540px; height: 316px;
    background: var(--frame);
    padding: 14px;
    box-shadow: 0 6px 18px rgba(0,0,0,.18);
  }
  .card__frame {
    width: 100%; height: 100%;
    border: 2px solid var(--frame-line);
    padding: 4px;
  }
  /* Front */
  .front__face {
    width: 100%; height: 100%;
    background: radial-gradient(ellipse at 45% 45%, var(--face-light) 0%, var(--face-mid) 100%);
    display: flex; align-items: center; justify-content: center;
  }
  .brand { display: flex; align-items: center; gap: 16px; }
  .brand__mark { width: 40px; height: 40px; background: var(--brand-blue); }
  .brand__name {
    font-weight: 700; font-size: 32px; color: var(--brand-deep);
    letter-spacing: 1px; text-transform: uppercase;
  }
  /* Back */
  .back__face {
    width: 100%; height: 100%;
    background: var(--white);
    display: flex; gap: 8px; padding: 6px;
  }
  .contacts { flex: 0 0 56%; display: flex; flex-direction: column; gap: 6px; }
  .contact {
    flex: 1; background: var(--row);
    display: flex; align-items: center; gap: 14px; padding-left: 16px;
  }
  .contact__icon {
    width: 44px; height: 44px; background: var(--brand-blue);
    display: flex; align-items: center; justify-content: center;
  }
  .contact__text { font-size: 14px; color: var(--ink); }
  .identity {
    flex: 1; background: var(--brand-blue); padding: 6px;
  }
  .identity__inner {
    width: 100%; height: 100%;
    border: 2px solid var(--white);
    display: flex; flex-direction: column; align-items: center; justify-content: center;
    color: var(--white); text-align: center;
  }
  .identity__name { font-size: 16px; }
  .identity__role { font-size: 10px; margin-top: 3px; }
</style>
</head>
<body>
<main class="canvas">
  <section class="card card--front" aria-label="Card front">
    <div class="card__frame">
      <div class="front__face">
        <div class="brand">
          <span class="brand__mark" aria-hidden="true"></span>
          <span class="brand__name">Velvor IT Services</span>
        </div>
      </div>
    </div>
  </section>

  <section class="card card--back" aria-label="Card back">
    <div class="card__frame">
      <div class="back__face">
        <ul class="contacts" style="list-style:none">
          <li class="contact">
            <span class="contact__icon">
              <svg width="22" height="22" viewBox="0 0 24 24" aria-hidden="true"><path fill="#fff" d="M6.6 10.8a15.1 15.1 0 0 0 6.6 6.6l2.2-2.2c.3-.3.7-.4 1-.2 1.1.4 2.3.6 3.6.6.6 0 1 .4 1 1V20c0 .6-.4 1-1 1A17 17 0 0 1 3 4c0-.6.4-1 1-1h3.5c.6 0 1 .4 1 1 0 1.3.2 2.5.6 3.6.1.3 0 .7-.2 1z"/></svg>
            </span>
            <span class="contact__text">0483 906 452</span>
          </li>
          <li class="contact">
            <span class="contact__icon">
              <svg width="24" height="18" viewBox="0 0 24 18" aria-hidden="true"><rect x="1" y="1" width="22" height="16" fill="#fff"/><path d="M1 1l11 9 11-9" fill="none" stroke="#3a9ad9" stroke-width="1.6"/></svg>
            </span>
            <span class="contact__text">support@velvorit.com.au</span>
          </li>
          <li class="contact">
            <span class="contact__icon">
              <svg width="24" height="24" viewBox="0 0 24 24" aria-hidden="true"><g fill="none" stroke="#fff" stroke-width="1.6"><circle cx="12" cy="12" r="9.5"/><ellipse cx="12" cy="12" rx="4.2" ry="9.5"/><path d="M2.5 12h19M4 7h16M4 17h16"/></g></svg>
            </span>
            <span class="contact__text">www.velvorit.com.au</span>
          </li>
        </ul>
        <div class="identity">
          <div class="identity__inner">
            <p class="identity__name">Marcus Dredge</p>
            <p class="identity__role">Director</p>
          </div>
        </div>
      </div>
    </div>
  </section>
</main>
</body>
</html>
```